Crestfield Slab & Tile Needs a Business Card

Attached you will find your logo, my photo and design guidelines for a new business card. The final design will need two separate files to create an embossed card. The cards will be printed by www.plimbo.com (Instructions below)
Format is the Plimbo SQUARE card
Crestfield Slab And Tile is a brick and mortar, retail stone and tile shop.
One the front:
Crestfield Slab And Tile
Gerald Pennock
Owner
48207 Dunmore Ridge Blvd
Suite R & T
Fernhollow, NC 28890
Cell: 704-555-0183
Web: www.CrestfieldSlabAndTile.com
(Make each word of the domain a different or alternating color)
On the back;
Something that shows beautiful colorful tile
Follow the design guide closely please. For more information see this page that describes creating the spot gloss file: https://www.plimbo.com/us/business-cards/design-guidelines-spot-gloss
The logo is what we would like to have raised spot glossed.
Contact Information for Business Card
Format is the Plimbo SQUARE card. See attahced guidlines.

```html
<!DOCTYPE html>
<html lang="en">
<head>
<meta charset="utf-8">
<title>Crestfield Slab &amp; Tile — Square Business Card</title>
<link rel="stylesheet" href="https://fonts.googleapis.com/css2?family=Cormorant+Garamond:ital,wght@0,400;0,500;0,700;1,500&display=swap">
<style>
  :root {
    --page: #f5f5fa;
    --card: #f1eee9;
    --paper: #ffffff;
    --rust: #a8401f;
    --slate: #2f3d44;
    --sage: #6b7560;
    --mustard: #d4952a;
    --ink: #3a3a3a;
    --black: #111111;
    --tile-beige: #c7b8a2;
    --tile-green: #4c6a3e;
    --tile-dark: #22323a;
  }
  * { box-sizing: border-box; margin: 0; padding: 0; }
  html, body { width: 1178px; height: 1200px; overflow: hidden; background: var(--page); }
  body { position: relative; font-family: "Cormorant Garamond", Georgia, serif; color: var(--ink); }

  .card {
    position: absolute; width: 458px; height: 458px; overflow: hidden;
    box-shadow: 0 16px 20px -6px rgba(0,0,0,.14);
  }
  .card--front { left: 108px; top: 108px; background: var(--card); }
  .card--back  { left: 613px; top: 108px; background: var(--card); }
  .card--gloss-front { left: 108px; top: 613px; background: var(--paper); }
  .card--gloss-back  { left: 613px; top: 613px; background: var(--paper); }

  /* wordmark */
  .wordmark { position: absolute; display: flex; align-items: center; gap: 12px; color: var(--slate); }
  .wordmark__square { width: 46px; height: 46px; background: currentColor; flex: none; }
  .wordmark__name { font-weight: 500; font-size: 20px; line-height: 1.05; letter-spacing: 2.5px; text-transform: uppercase; }
  .wordmark--front { right: 28px; top: 28px; }
  .wordmark--back { right: 30px; top: 40px; flex-direction: column; gap: 16px; text-align: center; }
  .wordmark--back .wordmark__square { width: 80px; height: 80px; }
  .wordmark--back .wordmark__name { font-size: 30px; letter-spacing: 4px; }
  .wordmark--ink { color: var(--black); }

  /* tile pattern areas */
  .tile-fill { position: absolute; }
  .tile-fill--corner-top {
    left: 0; top: 0; width: 150px; height: 130px;
    background: linear-gradient(135deg, #a9a6a1 0%, #d8c6b9 45%, rgba(241,238,233,0) 100%);
    clip-path: polygon(0 0, 100% 0, 0 100%);
    opacity: .85;
  }
  .tile-fill--corner-bottom {
    right: 0; bottom: 0; width: 150px; height: 96px;
    background: linear-gradient(315deg, #a9a6a1 0%, #d8c6b9 45%, rgba(241,238,233,0) 100%);
    clip-path: polygon(100% 0, 100% 100%, 0 100%);
    opacity: .85;
  }
  .tile-fill--hero {
    left: 0; top: 0; width: 458px; height: 458px;
    background: linear-gradient(135deg, var(--tile-beige) 0%, var(--tile-dark) 35%, var(--tile-green) 55%, #3f4a4a 75%, var(--tile-beige) 100%);
    clip-path: polygon(0 0, 80px 0, 285px 330px, 220px 458px, 0 458px);
  }

  /* name block */
  .person { position: absolute; right: 28px; top: 102px; text-align: right; }
  .person__name { font-weight: 700; font-size: 31px; color: var(--rust); line-height: 1; }
  .person__role { font-weight: 500; font-size: 19px; letter-spacing: 1.5px; color: var(--ink); text-align: center; margin-top: 4px; }

  .rule { position: absolute; right: 0; height: 4px; }
  .rule--sage { left: 79px; top: 166px; background: var(--sage); }
  .rule--slate { left: 184px; top: 180px; background: var(--slate); }

  /* contact rows */
  .contact { position: absolute; left: 0; display: flex; align-items: center; }
  .contact__icon { width: 67px; height: 42px; display: flex; align-items: center; justify-content: center; flex: none; }
  .contact__icon svg { width: 22px; height: 22px; fill: none; stroke: #fff; stroke-width: 1.6; stroke-linecap: round; stroke-linejoin: round; }
  .contact__text { margin-left: 14px; font-size: 20px; font-weight: 500; line-height: 1.35; }
  .contact--address { top: 224px; }
  .contact--address .contact__icon { background: var(--rust); }
  .contact--phone { top: 297px; }
  .contact--phone .contact__icon { background: var(--slate); }
  .contact--web { top: 371px; }
  .contact--web .contact__icon { background: var(--mustard); }
  .contact--web .contact__text { font-style: italic; font-size: 19px; }
  .web--dark { color: var(--slate); }
  .web--rust { color: var(--rust); }
  .web--mustard { color: var(--mustard); }
</style>
</head>
<body>

  <!-- card front -->
  <section class="card card--front">
    <div class="tile-fill tile-fill--corner-top" role="img" aria-label="Scattered square tile pattern in soft greys, blush and sage"></div>
    <div class="tile-fill tile-fill--corner-bottom" role="img" aria-label="Scattered square tile pattern in soft greys, blush and sage"></div>

    <div class="wordmark wordmark--front">
      <span class="wordmark__square"></span>
      <span class="wordmark__name">Crestfield<br>Slab &amp; Tile</span>
    </div>

    <div class="person">
      <p class="person__name">Gerald Pennock</p>
      <p class="person__role">Owner</p>
    </div>

    <div class="rule rule--sage"></div>
    <div class="rule rule--slate"></div>

    <div class="contact contact--address">
      <span class="contact__icon">
        <svg viewBox="0 0 24 24"><path d="M3 11 12 3l9 8"/><path d="M5 10v10h14V10"/><path d="M10 20v-6h4v6"/></svg>
      </span>
      <p class="contact__text">48207 Dunmore Ridge Blvd<br>Suite R &amp; T | Fernhollow, NC 28890</p>
    </div>

    <div class="contact contact--phone">
      <span class="contact__icon">
        <svg viewBox="0 0 24 24"><path d="M5 3h4l2 5-2.5 1.5a11 11 0 0 0 6 6L16 13l5 2v4a2 2 0 0 1-2 2A16 16 0 0 1 3 5a2 2 0 0 1 2-2z"/></svg>
      </span>
      <p class="contact__text">704-555-0183</p>
    </div>

    <div class="contact contact--web">
      <span class="contact__icon">
        <svg viewBox="0 0 24 24"><circle cx="12" cy="12" r="9"/><path d="M3 12h18"/><path d="M12 3a14 14 0 0 1 0 18a14 14 0 0 1 0-18z"/></svg>
      </span>
      <p class="contact__text"><span class="web--dark">www.</span><span class="web--rust">Crestfield</span><span class="web--dark">Slab</span><span class="web--mustard">And</span><span class="web--dark">Tile.com</span></p>
    </div>
  </section>

  <!-- card back -->
  <section class="card card--back">
    <div class="tile-fill tile-fill--hero" role="img" aria-label="Cascade of overlapping square tiles in slate, beige, green and rust"></div>
    <div class="wordmark wordmark--back">
      <span class="wordmark__square"></span>
      <span class="wordmark__name">Crestfield<br>Slab &amp; Tile</span>
    </div>
  </section>

  <!-- spot gloss layer, front -->
  <section class="card card--gloss-front">
    <div class="wordmark wordmark--front wordmark--ink">
      <span class="wordmark__square"></span>
      <span class="wordmark__name">Crestfield<br>Slab &amp; Tile</span>
    </div>
  </section>

  <!-- spot gloss layer, back -->
  <section class="card card--gloss-back">
    <div class="wordmark wordmark--back wordmark--ink">
      <span class="wordmark__square"></span>
      <span class="wordmark__name">Crestfield<br>Slab &amp; Tile</span>
    </div>
  </section>

</body>
</html>
```